1/2 Page add for BRMTL Conference

We are looking for a 1/2 page ad to support the annual BRMTL conference. I want to encourage the attendees to come to our both so we can explain how they can save money on food and supplies. here is a link to the conference. https://www.brmtl-example.org/conference/ here is our website www.pantrywisehub-example.com - the what we do can be captured in the ad. We will be at booth 505. Our goal is to get people to our BOOTH #214 to explain the services that we provide –

Discounted food pricing
Free menu planning/design
Use of Registered Dietitian
Huge selection of discounted PPE and other necessary supplies to run any child care center

We have over 6000 members in 46 States and work with both small and large food distributors. We have been a sponsor of the association for the last 10 years.

Target Market(s)

Child care centers

Requirements
Must have
• Booth number -outline of what we do --- Stress we are a FREE service getting our members reduced pricing on food and supplies

```html
<!DOCTYPE html>
<html lang="en">
<head>
<meta charset="utf-8">
<title>PantryWise Hub – Conference Booth Ad</title>
<link rel="stylesheet" href="https://fonts.googleapis.com/css2?family=Open+Sans:ital,wght@0,400;0,600;0,700;0,800;1,700&display=swap">
<style>
  :root {
    --page-bg: #e4e4e4;
    --card-bg: #ffffff;
    --green-light: #9ccc3c;
    --green-dark: #4f9f3a;
    --brand-blue: #4a86c8;
    --teal: #2aa58f;
    --orange: #f5a623;
    --logo-grey: #6d6e71;
    --photo-tone-a: #e9e2d8;
    --photo-tone-b: #b9cf9a;
    --food-tone-a: #e0572b;
    --food-tone-b: #6fae3e;
    --white: #ffffff;
  }
  * { margin: 0; padding: 0; box-sizing: border-box; }
  html, body {
    width: 1200px; height: 850px; overflow: hidden;
    background: var(--page-bg);
    font-family: "Open Sans", Arial, sans-serif;
  }
  .ad-card {
    position: absolute; left: 30px; top: 49px;
    width: 1140px; height: 752px;
    background: var(--card-bg);
    overflow: hidden;
  }
  .ad-shapes { position: absolute; inset: 0; }
  .booth-tag {
    position: absolute; left: 880px; top: 0; width: 240px; height: 54px;
    background: var(--white); border-radius: 0 0 10px 10px;
    color: var(--brand-blue); font-weight: 800; font-size: 30px;
    display: flex; align-items: center; justify-content: center; letter-spacing: 0.5px;
  }
  .conference-name {
    position: absolute; right: 30px; top: 66px;
    color: var(--white); font-style: italic; font-weight: 700; font-size: 23px;
  }
  .headline {
    position: absolute; right: 30px; top: 98px; text-align: right;
    color: var(--white); font-weight: 800; font-size: 46px; line-height: 57px;
    letter-spacing: -0.5px;
  }
  .service-list { position: absolute; right: 25px; top: 220px; width: 530px; list-style: none; }
  .service-item {
    height: 61px; display: flex; align-items: center; justify-content: flex-end; gap: 14px;
    color: var(--white); font-size: 26px;
    border-bottom: 2px dotted rgba(255,255,255,0.7);
  }
  .service-item:last-child { border-bottom: none; }
  .service-icon { width: 56px; height: 56px; flex: none; }
  .free-note {
    position: absolute; right: 25px; top: 532px; text-align: right;
    color: var(--white); font-style: italic; font-weight: 700; font-size: 21px; line-height: 27px;
  }
  .event-details {
    position: absolute; right: 25px; top: 652px; text-align: right;
    color: var(--white); font-size: 24px; line-height: 30px;
  }
  .event-url { font-weight: 700; }
  .brand {
    position: absolute; left: 60px; top: 680px;
    display: flex; align-items: center; gap: 14px;
  }
  .brand-mark { width: 40px; height: 40px; background: var(--brand-blue); }
  .brand-name { color: var(--logo-grey); font-size: 38px; font-weight: 400; }
</style>
</head>
<body>
<div class="ad-card">
  <svg class="ad-shapes" width="1140" height="752" viewBox="0 0 1140 752">
    <defs>
      <linearGradient id="green-panel" x1="0" y1="0" x2="1" y2="0">
        <stop offset="0" stop-color="var(--green-light)"/>
        <stop offset="1" stop-color="var(--green-dark)"/>
      </linearGradient>
      <linearGradient id="photo-fill" x1="0" y1="0" x2="1" y2="1">
        <stop offset="0" stop-color="var(--photo-tone-a)"/>
        <stop offset="1" stop-color="var(--photo-tone-b)"/>
      </linearGradient>
      <linearGradient id="food-fill" x1="0" y1="0" x2="1" y2="1">
        <stop offset="0" stop-color="var(--food-tone-a)"/>
        <stop offset="1" stop-color="var(--food-tone-b)"/>
      </linearGradient>
    </defs>
    <path d="M380 0 H1140 V641 H380 Z" fill="url(#green-panel)"/>
    <path d="M527 752 C560 680 610 641 700 641 H1140 V752 Z" fill="var(--brand-blue)"/>
    <ellipse cx="60" cy="40" rx="85" ry="90" fill="var(--teal)"/>
    <ellipse cx="270" cy="4" rx="70" ry="26" fill="var(--orange)"/>
    <ellipse cx="30" cy="560" rx="45" ry="40" fill="var(--orange)"/>
    <ellipse cx="360" cy="640" rx="40" ry="26" fill="var(--orange)"/>
    <circle cx="204" cy="318" r="334" fill="var(--white)"/>
    <circle cx="204" cy="318" r="318" fill="none" stroke="var(--brand-blue)" stroke-width="8"/>
    <circle cx="204" cy="318" r="306" fill="url(#photo-fill)" role="img"
            aria-label="Photo of three smiling children holding fresh vegetables and fruit"/>
    <circle cx="470" cy="508" r="86" fill="var(--white)"/>
    <circle cx="470" cy="508" r="72" fill="url(#food-fill)" role="img"
            aria-label="Heart-shaped arrangement of fresh fruit and vegetables"/>
  </svg>

  <div class="booth-tag">BOOTH #214</div>
  <p class="conference-name">2022 Regional Kids Meal Service Summit</p>
  <h1 class="headline">SAVE MONEY ON FOOD<br>AND SUPPLIES</h1>

  <ul class="service-list">
    <li class="service-item">Discounted food pricing
      <svg class="service-icon" viewBox="0 0 58 58"><circle cx="29" cy="29" r="27" fill="var(--brand-blue)" stroke="#fff" stroke-width="3"/><path d="M20 36 L32 18 H40 V26 L28 42 Z" fill="none" stroke="#fff" stroke-width="2.5" stroke-linejoin="round"/><circle cx="36" cy="22" r="2" fill="#fff"/></svg>
    </li>
    <li class="service-item">Free menu planning/design
      <svg class="service-icon" viewBox="0 0 58 58"><circle cx="29" cy="29" r="27" fill="var(--brand-blue)" stroke="#fff" stroke-width="3"/><path d="M16 35 A13 13 0 0 1 42 35 Z" fill="#fff"/><rect x="13" y="36" width="32" height="3" rx="1.5" fill="#fff"/><circle cx="29" cy="20" r="2.5" fill="#fff"/></svg>
    </li>
    <li class="service-item">Use of Registered Dietitian
      <svg class="service-icon" viewBox="0 0 58 58"><circle cx="29" cy="29" r="27" fill="var(--brand-blue)" stroke="#fff" stroke-width="3"/><circle cx="29" cy="22" r="6" fill="none" stroke="#fff" stroke-width="2.5"/><path d="M19 42 C19 33 39 33 39 42" fill="none" stroke="#fff" stroke-width="2.5"/></svg>
    </li>
    <li class="service-item">Huge selection of discounted PPE
      <svg class="service-icon" viewBox="0 0 58 58"><circle cx="29" cy="29" r="27" fill="var(--brand-blue)" stroke="#fff" stroke-width="3"/><path d="M22 42 V24 M26 42 V16 M30 42 V16 M34 42 V20 M22 42 H36 L40 30" fill="none" stroke="#fff" stroke-width="2.5" stroke-linecap="round"/></svg>
    </li>
    <li class="service-item">Supplies to run any child care center
      <svg class="service-icon" viewBox="0 0 58 58"><circle cx="29" cy="29" r="27" fill="var(--brand-blue)" stroke="#fff" stroke-width="3"/><rect x="18" y="18" width="14" height="24" fill="none" stroke="#fff" stroke-width="2.5"/><rect x="32" y="27" width="9" height="15" fill="none" stroke="#fff" stroke-width="2.5"/><path d="M22 24 H28 M22 30 H28 M22 36 H28" stroke="#fff" stroke-width="2"/></svg>
    </li>
  </ul>

  <p class="free-note">We are a FREE service getting our members<br>reduced pricing on food and supplies</p>

  <div class="event-details">
    <p>MAY 9-13, 2022</p>
    <p>Riverton, Lakeshire</p>
    <p class="event-url">www.pantrywisehub-example.com</p>
  </div>

  <div class="brand">
    <span class="brand-mark"></span>
    <span class="brand-name">PantryWise Hub</span>
  </div>
</div>
</body>
</html>
```